Looking for awesome business card design with attached existing logo

We are a water, mold, and fire damage restoration company called "Torvane Seco" Looking for an awesome business card that is edgy yet professional and unique. Show me what you got!

```html
<!DOCTYPE html>
<html lang="en">
<head>
<meta charset="utf-8">
<title>Torvane Seco — Business Card</title>
<link href="https://fonts.googleapis.com/css2?family=Montserrat:wght@600;700&family=Open+Sans:wght@400;600&display=swap" rel="stylesheet">
<style>
  :root {
    --bg: #e9e6e1;
    --card-white: #ffffff;
    --teal: #264b59;
    --teal-deep: #1d3d49;
    --amber: #d8922b;
    --rust: #c4432e;
    --gold: #d39a2c;
    --text-light: #ffffff;
    --rule: #b08a3a;
  }
  * { box-sizing: border-box; margin: 0; padding: 0; }
  html, body {
    width: 1200px; height: 900px; overflow: hidden;
    background: var(--bg);
  }
  .stage {
    width: 1200px; height: 900px;
    display: flex; flex-direction: column; align-items: center; justify-content: center;
    gap: 60px;
  }
  .card {
    position: relative;
    width: 560px; height: 320px;
    background: var(--card-white);
    overflow: hidden;
    box-shadow: 0 10px 28px rgba(0,0,0,0.18);
  }
  .card-art { position: absolute; inset: 0; width: 100%; height: 100%; }

  .brand {
    position: absolute;
    display: flex; align-items: center; gap: 12px;
    font-family: "Montserrat", sans-serif;
    font-weight: 700;
    color: var(--teal);
    letter-spacing: 0.02em;
    white-space: nowrap;
    z-index: 1;
  }
  .brand-dot {
    width: 22px; height: 22px; border-radius: 50%;
    background: var(--gold);
    flex: none;
  }
  .card--front .brand { right: 36px; top: 118px; font-size: 28px; }
  .card--back .brand { left: 36px; top: 140px; font-size: 28px; }

  .front-url {
    position: absolute;
    left: 36px; top: 160px;
    transform: translate(-50%, -50%) rotate(90deg);
    transform-origin: center;
    font-family: "Open Sans", sans-serif;
    font-weight: 600;
    font-size: 13px;
    letter-spacing: 0.32em;
    color: var(--text-light);
    white-space: nowrap;
  }
  .front-url .accent { color: var(--gold); }

  .contact {
    position: absolute;
    right: 28px; top: 50px;
    width: 230px;
    text-align: right;
    font-family: "Open Sans", sans-serif;
    color: var(--text-light);
  }
  .contact-role { font-size: 13px; }
  .contact-name {
    font-family: "Montserrat", sans-serif;
    font-weight: 700; font-size: 15px;
    color: var(--amber);
    letter-spacing: 0.03em;
    margin-bottom: 26px;
  }
  .contact-line {
    display: flex; justify-content: flex-end; align-items: center; gap: 8px;
    font-size: 13px; line-height: 22px;
  }
  .contact-icon { width: 13px; height: 13px; flex: none; }
  .contact-rule {
    height: 1px; background: var(--rule);
    margin: 8px 0 8px 20px;
  }
  .contact-address { font-size: 13px; text-align: left; padding-left: 20px; }
</style>
</head>
<body>
<main class="stage">

  <section class="card card--front" aria-label="Card front">
    <svg class="card-art" viewBox="0 0 560 320" preserveAspectRatio="none" aria-hidden="true">
      <defs>
        <linearGradient id="bandFront" x1="0" y1="0" x2="0.6" y2="1">
          <stop offset="0" stop-color="#d8922b"/>
          <stop offset="1" stop-color="#c4432e"/>
        </linearGradient>
      </defs>
      <path d="M0,0 L95,0 C110,60 160,95 215,115 C265,135 275,190 265,250 L255,320 L0,320 Z" fill="url(#bandFront)"/>
      <path d="M0,0 L75,0 C90,65 140,100 190,120 C240,140 248,195 238,252 L228,320 L0,320 Z" fill="var(--teal-deep)"/>
      <path d="M0,0 L66,0 C80,68 130,104 180,124 C228,144 236,198 226,254 L216,320 L0,320 Z" fill="var(--teal)"/>
    </svg>
    <p class="front-url">www<span class="accent">.torvaneseco.</span>com</p>
    <div class="brand"><span class="brand-dot"></span>Torvane Seco</div>
  </section>

  <section class="card card--back" aria-label="Card back">
    <svg class="card-art" viewBox="0 0 560 320" preserveAspectRatio="none" aria-hidden="true">
      <defs>
        <linearGradient id="bandBack" x1="0" y1="0" x2="0.3" y2="1">
          <stop offset="0" stop-color="#d8922b"/>
          <stop offset="1" stop-color="#c4432e"/>
        </linearGradient>
      </defs>
      <path d="M240,0 L560,0 L560,320 L395,320 C340,300 300,255 296,190 C292,120 320,70 285,25 C275,12 260,4 240,0 Z" fill="url(#bandBack)"/>
      <path d="M268,0 L560,0 L560,320 L430,320 C380,298 345,255 342,195 C339,130 360,75 325,30 C313,15 295,5 268,0 Z" fill="var(--teal-deep)"/>
      <path d="M282,0 L560,0 L560,320 L446,320 C398,298 362,256 360,198 C357,134 378,80 342,32 C330,16 310,5 282,0 Z" fill="var(--teal)"/>
    </svg>
    <div class="brand"><span class="brand-dot"></span>Torvane Seco</div>

    <div class="contact">
      <p class="contact-role">Director</p>
      <p class="contact-name">MARLO FENWICK</p>
      <p class="contact-line">555-014-2287
        <svg class="contact-icon" viewBox="0 0 16 16"><path fill="#c4432e" d="M3.5 1.5l2.5 0 1.2 3.2-1.6 1.2c.8 1.7 2.1 3 3.8 3.8l1.2-1.6 3.2 1.2 0 2.5c0 .8-.7 1.5-1.5 1.5C6.6 13.3 2.7 9.4 2 3c0-.8.7-1.5 1.5-1.5z"/></svg>
      </p>
      <p class="contact-line">info@torvaneseco.com
        <svg class="contact-icon" viewBox="0 0 16 16"><rect x="1.5" y="3.5" width="13" height="9" rx="1.5" fill="#c4432e"/><path d="M2.5 4.5l5.5 4 5.5-4" fill="none" stroke="#fff" stroke-width="1.2"/></svg>
      </p>
      <p class="contact-line">www.torvaneseco.com
        <svg class="contact-icon" viewBox="0 0 16 16"><circle cx="8" cy="8" r="6.5" fill="none" stroke="#c4432e" stroke-width="1.5"/><ellipse cx="8" cy="8" rx="2.8" ry="6.5" fill="none" stroke="#c4432e" stroke-width="1.2"/><path d="M1.5 8h13" stroke="#c4432e" stroke-width="1.2"/></svg>
      </p>
      <div class="contact-rule"></div>
      <p class="contact-line contact-address">42 Harbor Lane, Millbrook 00
        <svg class="contact-icon" viewBox="0 0 16 16"><path fill="#c4432e" d="M8 1a5 5 0 0 1 5 5c0 3.6-5 9-5 9S3 9.6 3 6a5 5 0 0 1 5-5z"/><circle cx="8" cy="6" r="1.8" fill="#fff"/></svg>
      </p>
    </div>
  </section>

</main>
</body>
</html>
```